CBD Banner Ad for Print and Plimbo

I we would like a modern European chic that we can use in a 1/4 page ad in our local magazine and also use as our banner ad in the Plimbo ad searches. <br/><br/>We are a high end CBD boutique shop that has their own brand as well as a carefully curated selection of the top end CBD products out on the market. The final design should promote the health and well being that we are trying to live ourselves. We DO NOT want the use of marijuana paraphernalia or like substances. Think Yoga Studio meets Morvette inside of a health store. <br/><br/>Use any images you would like...I have attached a sample product render as well as the inside of our store...but take this in the direction you would like.<br/><br/>The winner will have the added bonus of being able to create 10 more ads for us in the next 6 months.

Target Market(s)

Our target market are the middle to upperclass professional workers that want to take CBD but were afraid due to misinformation or stigma

Font styles to use
Sans Serif

Colors
33b8a4
86cfc6
0792cd
3277b5
85acd3

Requirements
Must have
• A good clean modern design.
• Natural. Organic. Crisp. Welcoming.
Nice to have
• Tess Hollow
• CBD for wellness. CBD for life.
• The font we use for the rest of our campaigns is Adam.
Should not have
• Absolutely NO marijuana leaves, paraphernalia, or references. We are working hard to educate people and get rid of the stigma.

```html
<!DOCTYPE html>
<html lang="en">
<head>
<meta charset="utf-8">
<title>Tess Hollow – CBD Gummies Ad</title>
<link href="https://fonts.googleapis.com/css2?family=Cormorant+Garamond:wght@400&family=Josefin+Sans:wght@300;700&family=Montserrat:wght@300&display=swap" rel="stylesheet">
<style>
  :root {
    --ink-dark: #141414;
    --store-mid: #3c3d42;
    --floor: #55504c;
    --white: #ffffff;
    --pack-white: #f7f7f8;
    --pack-lilac: #d9d6ef;
    --pack-sand: #ece3d2;
    --gold: #c2ab7c;
    --gold-text: #b9a27a;
    --gold-ink: #3a342c;
    --pack-ink: #1e1e1e;
    --pack-grey: #444444;
  }
  html, body {
    margin: 0;
    padding: 0;
    width: 900px;
    height: 1200px;
    overflow: hidden;
    background: var(--ink-dark);
  }
  .ad {
    position: relative;
    width: 900px;
    height: 1200px;
    overflow: hidden;
  }
  .store-scene {
    position: absolute;
    inset: 0;
    background: linear-gradient(180deg, var(--ink-dark) 0%, #232325 22%, var(--store-mid) 48%, #4a4746 70%, var(--floor) 100%);
  }
  .brand-name {
    position: absolute;
    left: 88px;
    top: 205px;
    margin: 0;
    font-family: "Josefin Sans", sans-serif;
    font-weight: 300;
    font-size: 56px;
    letter-spacing: 3px;
    text-transform: uppercase;
    color: var(--white);
    white-space: nowrap;
  }
  .product {
    position: absolute;
    box-shadow: 0 14px 30px rgba(0,0,0,0.35);
  }
  .product-shape {
    position: absolute;
    inset: 0;
    border-radius: inherit;
    background: linear-gradient(160deg, var(--pack-white) 0%, var(--pack-white) 60%, var(--pack-sand) 80%, var(--pack-lilac) 100%);
  }
  .product-jar {
    left: 56px;
    top: 440px;
    width: 354px;
    height: 597px;
    border-radius: 28px 28px 18px 18px;
  }
  .product-compact {
    left: 426px;
    top: 685px;
    width: 348px;
    height: 369px;
    border-radius: 90px;
  }
  .pack-label {
    position: absolute;
    left: 0;
    right: 0;
    margin: 0;
    text-align: center;
    white-space: nowrap;
  }
  .pack-brand {
    font-family: "Josefin Sans", sans-serif;
    font-weight: 300;
    text-transform: uppercase;
    color: var(--gold-text);
    letter-spacing: 2px;
  }
  .pack-title {
    font-family: "Josefin Sans", sans-serif;
    font-weight: 700;
    text-transform: uppercase;
    color: var(--pack-ink);
    letter-spacing: 1.5px;
  }
  .pack-flavours {
    font-family: "Josefin Sans", sans-serif;
    font-weight: 300;
    text-transform: uppercase;
    color: var(--pack-grey);
    letter-spacing: 1px;
  }
  .pack-strength {
    font-family: "Josefin Sans", sans-serif;
    font-weight: 700;
    text-transform: uppercase;
    color: var(--pack-ink);
    letter-spacing: 1px;
    font-size: 12px;
    line-height: 17px;
  }
  .pack-count {
    font-family: "Cormorant Garamond", serif;
    font-weight: 400;
    color: var(--pack-grey);
    font-size: 14px;
  }
  .product-jar .pack-brand { top: 258px; font-size: 34px; }
  .product-jar .pack-title { top: 368px; font-size: 19px; }
  .product-jar .pack-flavours { top: 403px; font-size: 15px; }
  .product-jar .pack-strength { top: 446px; }
  .product-jar .pack-count { top: 522px; }
  .product-compact .pack-brand { top: 140px; font-size: 28px; }
  .product-compact .pack-title { top: 226px; font-size: 15px; }
  .contact-bar {
    position: absolute;
    left: 72px;
    top: 1093px;
    width: 748px;
    height: 59px;
    display: flex;
    gap: 5px;
  }
  .contact-item {
    flex: 1;
    display: flex;
    align-items: center;
    justify-content: center;
    background: var(--gold);
    color: var(--gold-ink);
    font-family: "Montserrat", sans-serif;
    font-weight: 300;
    font-size: 21px;
    white-space: nowrap;
  }
  .contact-item:first-child { border-radius: 30px 0 0 30px; }
  .contact-item:last-child { border-radius: 0 30px 30px 0; }
</style>
</head>
<body>
  <main class="ad">
    <div class="store-scene" role="img" aria-label="Photo of the bright boutique interior with shelves of products and potted plants"></div>
    <h1 class="brand-name">Tess Hollow</h1>

    <section class="product product-jar">
      <div class="product-shape" role="img" aria-label="Product render of a white jar of CBD gummies"></div>
      <p class="pack-label pack-brand">Tess Hollow</p>
      <p class="pack-label pack-title">CBD Gummies</p>
      <p class="pack-label pack-flavours">Grape . Orange. Lemon</p>
      <p class="pack-label pack-strength">300 mg<br>Phytocannabinoid<br>CBD</p>
      <p class="pack-label pack-count">(30) 10 MG GUMMIES</p>
    </section>

    <section class="product product-compact">
      <div class="product-shape" role="img" aria-label="Product render of a white square travel pack of CBD gummies"></div>
      <p class="pack-label pack-brand">Tess Hollow</p>
      <p class="pack-label pack-title">CBD Gummies</p>
    </section>

    <div class="contact-bar">
      <span class="contact-item">hi@tesshollow.com</span>
      <span class="contact-item">602-555-0148</span>
      <span class="contact-item">www.tesshollow.com</span>
    </div>
  </main>
</body>
</html>
```